card design for engineering consultancy

engineering drafting and project management company the provides drafting services for.
Electrical, Hydraulic, Mechanical, and Civil services
The company is called K7R Services and logo is as attached
Information on card should be.
1. Logo
2.website : K7RServices.com
3. email : info@K7RServices.com
4. Phone: (+61) 400512738
5. Motto: Design - Document - Develop - Deliver

this card should be basically used for business identification only

Target Market(s)

electricians plumbers air conditioning installers and civil contractors

Industry/Entity Type

engineering, drafting, electrical, plumbing, airconditioning, civil

Contact Information for Business Card

1. Logo 2.website : K7RServices.com 3. email : info@K7RServices.com 4. Phone: (+61) 400512738 5. Motto: Design - Document - Develop - Deliver

Font styles to use
Serif

Requirements
Must have
• logo
Nice to have
• something inovative and different that makes it stand out from being just another business card

```html
<!DOCTYPE html>
<html lang="en">
<head>
<meta charset="utf-8">
<title>K7R Services – Business Card</title>
<link href="https://fonts.googleapis.com/css2?family=Arimo:wght@400;700&display=swap" rel="stylesheet">
<style>
  :root {
    --backdrop: #e4e4e2;
    --card: #4e4b4b;
    --card-deep: #3a3838;
    --pattern-dark: #2f2e2e;
    --pattern-light: #6f6d6d;
    --white: #ffffff;
    --red: #c8161d;
    --rule: #bdbdbd;
  }
  * { box-sizing: border-box; margin: 0; padding: 0; }
  html, body {
    width: 1200px; height: 801px; overflow: hidden;
    background: var(--backdrop);
    font-family: "Arimo", Arial, sans-serif;
  }
  .sheet {
    position: relative; width: 1200px; height: 801px;
    display: flex; align-items: center; justify-content: center; gap: 40px;
  }
  .card {
    position: relative; width: 540px; height: 309px;
    background: var(--card); overflow: hidden;
    box-shadow: 0 6px 18px rgba(0,0,0,.18);
  }

  /* Front */
  .brand {
    position: absolute; left: 0; right: 0; top: 62px;
    display: flex; align-items: center; justify-content: center; gap: 16px;
  }
  .brand-mark { width: 46px; height: 46px; background: var(--red); }
  .brand-name {
    color: var(--white); font-weight: 700; font-size: 38px;
    letter-spacing: 3px; text-transform: uppercase;
  }
  .details {
    position: absolute; left: 0; right: 0; top: 176px;
    display: flex; justify-content: center; align-items: center; gap: 26px;
  }
  .person { text-align: right; }
  .person-name {
    color: var(--red); font-size: 21px; letter-spacing: 1px;
    text-transform: uppercase;
  }
  .person-role { color: var(--white); font-size: 15px; margin-top: 4px; }
  .divider { width: 1px; height: 78px; background: var(--rule); }
  .contacts { list-style: none; }
  .contacts li {
    display: flex; align-items: center; gap: 10px;
    color: var(--white); font-size: 14.5px; line-height: 25px;
  }
  .contacts svg { width: 13px; height: 13px; fill: var(--red); flex: none; }

  /* Back */
  .pattern {
    position: absolute; inset: 0;
    background: linear-gradient(120deg, var(--pattern-dark) 0%, var(--card-deep) 45%, var(--pattern-light) 100%);
  }
  .back-sign {
    position: absolute; right: 36px; bottom: 40px; text-align: right;
  }
  .back-brand { display: flex; align-items: center; justify-content: flex-end; gap: 12px; }
  .back-brand .brand-mark { width: 30px; height: 30px; }
  .back-brand .brand-name { font-size: 28px; letter-spacing: 2px; }
  .motto {
    margin-top: 8px; color: var(--white); font-size: 13px; font-weight: 700;
    letter-spacing: .5px; text-transform: uppercase;
  }
  .motto .dot { color: var(--red); margin: 0 3px; }
</style>
</head>
<body>
<main class="sheet">

  <section class="card card-front" aria-label="Card front">
    <div class="brand">
      <span class="brand-mark"></span>
      <span class="brand-name">K7R Services</span>
    </div>
    <div class="details">
      <div class="person">
        <p class="person-name">Daniel Harper</p>
        <p class="person-role">Manager</p>
      </div>
      <span class="divider"></span>
      <ul class="contacts">
        <li>
          <svg viewBox="0 0 24 24" aria-hidden="true"><path d="M6.6 10.8a15 15 0 0 0 6.6 6.6l2.2-2.2a1 1 0 0 1 1-.25 11.4 11.4 0 0 0 3.6.57 1 1 0 0 1 1 1V20a1 1 0 0 1-1 1A17 17 0 0 1 3 4a1 1 0 0 1 1-1h3.5a1 1 0 0 1 1 1c0 1.25.2 2.45.57 3.57a1 1 0 0 1-.25 1z"/></svg>
          (+61) 400512738
        </li>
        <li>
          <svg viewBox="0 0 24 24" aria-hidden="true"><path d="M2 5h20v14H2z M4 7v.5l8 5 8-5V7l-8 5z" fill-rule="evenodd"/></svg>
          info@K7RServices.com
        </li>
        <li>
          <svg viewBox="0 0 24 24" aria-hidden="true"><path d="M12 2a10 10 0 1 0 0 20 10 10 0 0 0 0-20zm0 2c.9 1.2 1.6 2.6 2 4h-4c.4-1.4 1.1-2.8 2-4zM4.3 14a8 8 0 0 1 0-4h3.4a16 16 0 0 0 0 4zm.9 2h3a14 14 0 0 0 1.3 3.6A8 8 0 0 1 5.2 16zm3-8h-3a8 8 0 0 1 4.3-3.6A14 14 0 0 0 8.2 8zM12 20c-.9-1.2-1.6-2.6-2-4h4c-.4 1.4-1.1 2.8-2 4zm2.3-6H9.7a14 14 0 0 1 0-4h4.6a14 14 0 0 1 0 4zm.2 5.6a14 14 0 0 0 1.3-3.6h3a8 8 0 0 1-4.3 3.6zm1.8-5.6a16 16 0 0 0 0-4h3.4a8 8 0 0 1 0 4z"/></svg>
          www.K7RServices.com
        </li>
      </ul>
    </div>
  </section>

  <section class="card card-back" aria-label="Card back">
    <div class="pattern" role="img" aria-label="Repeating embossed monogram pattern in dark and light greys"></div>
    <div class="back-sign">
      <div class="back-brand">
        <span class="brand-name">K7R Services</span>
        <span class="brand-mark"></span>
      </div>
      <p class="motto"><span class="dot">•</span>Design <span class="dot">•</span> Document <span class="dot">•</span> Develop <span class="dot">•</span> Deliver</p>
    </div>
  </section>

</main>
</body>
</html>
```